I need a flyer made , the flyer can be one page or two pages or three pages . I will be posting this on Instagram and social media platforms. I am a luxury home builder , I am looking to hire a construction project manager . Below are some examples and ideas what can be on the flyer

We’re looking for a construction project manager who’s passionate about building luxury homes at the highest standards
We’re hiring construction project manager
* Experience 5+ years in residential project management with a strong portfolio of completed homes.
* location : Bergen County NJ
* excellent leadership skills, leads teams with confidence and clarity
* communicates seamlessly with architects , engineers, designers and clients
*knows how to manage budgets and timelines without compromising quality
*solves problems with a positive solution first mindset
* pays attention to every detail because in luxury the small things are the big things

Apply now , link in bio or DM to connect.

My logo is attached, my web site www.ridgelanebuilders.com
My style is modern but still warm and inviting. I like a clean classy look .
Updates

Please don’t add any images of chairs or people to the flyer , I do not want people on my flyer. Do not add standard images of offices and houses , we are luxury builders , we build homes over 2 million dollars. Keep a classy , simple modern look . High end .

You can add a white hard hat with my logo on it for a image , this is a suggestion does not have to be on my flyer ,

```html
<!DOCTYPE html>
<html lang="en">
<head>
<meta charset="utf-8">
<title>We Are Hiring – Construction Project Manager</title>
<link href="https://fonts.googleapis.com/css2?family=Oxanium:wght@700;800&family=Roboto+Condensed:wght@700&family=Poppins:wght@400;500&family=Archivo:wght@800&display=swap" rel="stylesheet">
<style>
  :root{
    --bg:#f3f4f6;
    --ink:#0b0b0b;
    --paper:#ffffff;
    --muted:#8a8a8a;
    --ring:#e3e3e5;
    --soft:#e9e9ec;
  }
  html,body{margin:0;padding:0;overflow:hidden;background:var(--bg);}
  .flyer{position:relative;width:1200px;height:1200px;background:var(--bg);overflow:hidden;color:var(--ink);}
  .abs{position:absolute;}
  .bubble{left:0;top:0;}
  .headline{left:196px;top:104px;font-family:"Oxanium",sans-serif;font-weight:800;line-height:1;}
  .headline .small{font-size:42px;letter-spacing:1px;display:block;}
  .headline .big{font-size:142px;display:block;margin-top:4px;letter-spacing:2px;}
  .role-box{left:67px;top:431px;width:565px;height:108px;border:4px solid var(--ink);border-radius:14px;box-sizing:border-box;display:flex;align-items:center;padding-left:15px;background:var(--paper);}
  .role-box h2{margin:0;font-family:"Roboto Condensed",sans-serif;font-weight:700;font-size:39px;}
  .req-title{left:79px;top:585px;margin:0;font-family:"Oxanium",sans-serif;font-weight:800;font-size:38px;}
  .req-list{left:80px;top:656px;width:552px;margin:0;padding:0;list-style:none;font-family:"Poppins",sans-serif;font-size:17.5px;line-height:27.8px;}
  .req-list li{position:relative;padding-left:34px;margin-bottom:10px;}
  .req-list li.single{margin-bottom:9px;}
  .req-list svg{position:absolute;left:0;top:2px;width:16px;height:16px;}
  .apply{left:78px;top:1089px;width:187px;height:62px;background:var(--ink);color:var(--paper);display:flex;align-items:center;justify-content:center;font-family:"Archivo",sans-serif;font-weight:800;font-size:23px;letter-spacing:.5px;}
  .ring{border-radius:50%;border:3px solid var(--muted);width:30px;height:30px;}
  .halo{left:700px;top:485px;width:455px;height:455px;border-radius:50%;border:3px solid var(--ring);background:var(--paper);}
  .halo-small{left:1112px;top:1000px;width:120px;height:120px;border-radius:50%;background:var(--paper);}
  .arm-art{left:862px;top:505px;width:338px;height:210px;border-radius:18px 0 0 18px;background:linear-gradient(160deg,var(--paper) 0%,var(--soft) 100%);}
  .sign{left:727px;top:694px;width:316px;height:226px;border:3px solid #7a7a7a;background:var(--paper);box-sizing:border-box;display:flex;align-items:center;justify-content:center;text-align:center;font-family:"Archivo",sans-serif;font-weight:800;font-size:58px;line-height:1.02;}
  .brand{left:740px;top:1000px;width:360px;text-align:center;font-family:"Poppins",sans-serif;font-weight:500;color:var(--ink);line-height:1;}
  .brand .name{display:block;font-size:44px;letter-spacing:2px;}
  .brand .sub{display:block;font-size:26px;letter-spacing:3px;margin-top:10px;}
  .site{left:740px;top:1126px;width:360px;text-align:center;font-family:"Poppins",sans-serif;font-size:20px;}
</style>
</head>
<body>
<main class="flyer">
  <svg class="abs bubble" width="1200" height="420" viewBox="0 0 1200 420">
    <rect x="102" y="64" width="739" height="262" rx="26" fill="#ffffff"/>
    <polygon points="545,325 645,325 600,381" fill="#ffffff"/>
    <g fill="none" stroke="#0b0b0b" stroke-width="4" stroke-linecap="round">
      <path d="M72 205 V62 Q72 34 100 34 H633"/>
      <path d="M717 34 H838 Q867 34 867 62 V330 Q867 358 838 358 H680"/>
      <path d="M445 358 H100 Q72 358 72 330 V233"/>
    </g>
  </svg>

  <div class="abs headline">
    <span class="small">WE ARE</span>
    <span class="big">HIRING!</span>
  </div>

  <div class="abs role-box"><h2>Construction Project Manager</h2></div>

  <h3 class="abs req-title">Requirement :</h3>
  <ul class="abs req-list">
    <li><svg viewBox="0 0 16 16"><circle cx="7" cy="8.5" r="6" fill="none" stroke="#0b0b0b" stroke-width="1.4"/><path d="M4 8.5l3 3 7-8" fill="none" stroke="#0b0b0b" stroke-width="1.6"/></svg>Experience 5+ Years In Residential Project Management With A Strong Portfolio Of Completed Homes.</li>
    <li class="single"><svg viewBox="0 0 16 16"><circle cx="7" cy="8.5" r="6" fill="none" stroke="#0b0b0b" stroke-width="1.4"/><path d="M4 8.5l3 3 7-8" fill="none" stroke="#0b0b0b" stroke-width="1.6"/></svg>Location : Bergen County NJ</li>
    <li><svg viewBox="0 0 16 16"><circle cx="7" cy="8.5" r="6" fill="none" stroke="#0b0b0b" stroke-width="1.4"/><path d="M4 8.5l3 3 7-8" fill="none" stroke="#0b0b0b" stroke-width="1.6"/></svg>Excellent Leadership Skills, Leads Teams With Confidence And Clarity</li>
    <li><svg viewBox="0 0 16 16"><circle cx="7" cy="8.5" r="6" fill="none" stroke="#0b0b0b" stroke-width="1.4"/><path d="M4 8.5l3 3 7-8" fill="none" stroke="#0b0b0b" stroke-width="1.6"/></svg>Communicates Seamlessly With Architects , Engineers, Designers And Clients</li>
    <li><svg viewBox="0 0 16 16"><circle cx="7" cy="8.5" r="6" fill="none" stroke="#0b0b0b" stroke-width="1.4"/><path d="M4 8.5l3 3 7-8" fill="none" stroke="#0b0b0b" stroke-width="1.6"/></svg>Knows How To Manage Budgets And Timelines Without Compromising Quality</li>
    <li class="single"><svg viewBox="0 0 16 16"><circle cx="7" cy="8.5" r="6" fill="none" stroke="#0b0b0b" stroke-width="1.4"/><path d="M4 8.5l3 3 7-8" fill="none" stroke="#0b0b0b" stroke-width="1.6"/></svg>Solves Problems With A Positive Solution First Mindset</li>
    <li><svg viewBox="0 0 16 16"><circle cx="7" cy="8.5" r="6" fill="none" stroke="#0b0b0b" stroke-width="1.4"/><path d="M4 8.5l3 3 7-8" fill="none" stroke="#0b0b0b" stroke-width="1.6"/></svg>Pays Attention To Every Detail Because In Luxury The Small Things Are The Big Things</li>
  </ul>

  <div class="abs apply">APPLY NOW</div>

  <div class="abs halo"></div>
  <div class="abs halo-small"></div>
  <div class="abs ring" style="left:1139px;top:50px;"></div>
  <div class="abs ring" style="left:681px;top:650px;"></div>
  <div class="abs ring" style="left:19px;top:1144px;"></div>

  <div class="abs arm-art" role="img" aria-label="Illustration of a sleeved arm reaching in from the right to hold up the sign"></div>

  <div class="abs sign">JOIN OUR<br>TEAM</div>

  <div class="abs brand">
    <span class="name">RIDGELANE</span>
    <span class="sub">builders</span>
  </div>
  <div class="abs site">www.ridgelanebuilders.com</div>
</main>
</body>
</html>
```